UX interface for a Crypto currency payment gateway

This project requires you to open an account on our development web site http://dev.vorplin.com/cgi-bin/d

It requires you, as well, to download and install a Bitcoin client working on the testnet network (such as electrum), then get some Bitcoin testnet (those are free for who knows how to get them). "Simulate a payment" works as well.

This project requires you to know how to work with Bitcoins and cryptocurrencies.

Do NOT submit work if you're not interested in crypto-currencies.

Then, make some simulated payments on our development web site (Bitcoin testnet is only one supported crypto-currency there) to fill up a little bit the transaction report and the wallets.

Our UX sucks, yep, I know that, that's why we need you !

Then propose a design for the back office, first page is good enough (Accounts & Wallets).

You can change the layout as you see fit, the contest is as much about the UX design than the graphic design.

The price of the contest is for the best design of the first page only (Accounts & Wallets).

However, the winner will be required to code his design in HTML/CSS (JS may be required as well depending on your design) and he will get the whole back office and check out page to design and code in a one to one relationship with the customer (be prepared for a long term project). The winner will integrate his coding inside our templates.

Do NOT submit work if you're not interested to take the whole project or if you're not able to dedicate enough time to deliver a big quantity of work fast.
Updates

Requirements
Must have
• Design must look professional in "bank" style.

```html
<!DOCTYPE html>
<html lang="en">
<head>
<meta charset="utf-8">
<title>Coinvale – Accounts &amp; Wallet</title>
<link rel="stylesheet" href="https://fonts.googleapis.com/css2?family=Open+Sans:wght@400;600;700&family=Montserrat:wght@400;500;600&display=swap">
<style>
:root{
  --green:#157a2a;
  --green-dark:#116222;
  --page:#ebebed;
  --white:#ffffff;
  --ink:#222222;
  --muted:#4a4a4a;
  --line:#d6d6d6;
  --band:#ececee;
  --row-alt:#f6f6f6;
  --head:#efefef;
}
*{box-sizing:border-box;margin:0;padding:0}
html,body{width:1200px;height:868px;overflow:hidden}
body{background:var(--page);font-family:"Open Sans",sans-serif;color:var(--ink);position:relative}

/* header */
.topbar{position:absolute;left:0;top:0;width:1200px;height:75px;background:var(--white);box-shadow:0 1px 3px rgba(0,0,0,.08)}
.brand{position:absolute;left:120px;top:20px;display:flex;align-items:center;gap:8px}
.brand-dot{width:26px;height:26px;border-radius:50%;background:var(--green)}
.brand-name{font-family:"Open Sans",sans-serif;font-weight:600;font-size:20px;color:#2a2a2a;letter-spacing:.5px}
.nav{position:absolute;left:581px;top:0;height:75px;display:flex}
.nav-item{height:75px;display:flex;flex-direction:column;align-items:center;justify-content:center;gap:7px;font-family:"Montserrat",sans-serif;font-size:11px;color:#222;border-right:1px solid #eeeeee}
.nav-item svg{width:18px;height:18px}
.nav-item.active{background:var(--green);color:#fff;width:101px}
.nav-item.settings{width:96px}
.nav-item.notify{width:110px}
.nav-item.signout{width:96px;border-right:none}
.avatar{position:absolute;left:996px;top:15px;width:48px;height:48px;border-radius:50%;background:radial-gradient(circle at 50% 40%,#b98a6e,#5a3f33 70%,#2e2a28)}
.chev{position:absolute;left:1057px;top:37px}

/* panel */
.tabs{position:absolute;left:121px;top:122px;display:flex;gap:8px}
.tab{height:39px;width:142px;display:flex;align-items:center;justify-content:center;font-size:13px;background:var(--white);border:1px solid var(--line);border-bottom:none;color:#222}
.tab.active{background:var(--green);color:#fff;border-color:var(--green);width:151px}
.tab-rule{position:absolute;left:121px;top:160px;width:960px;height:4px;background:var(--green)}
.panel{position:absolute;left:121px;top:164px;width:960px;height:546px;background:var(--white);box-shadow:0 1px 3px rgba(0,0,0,.06)}

.sidebar{position:absolute;left:0;top:0;width:152px;height:546px;background:#f9f9f9;border-right:1px solid #e4e4e4}
.side-head{height:42px;background:var(--band);display:flex;align-items:center;padding-left:21px;font-weight:700;font-size:12.5px}
.side-link{height:44px;display:flex;align-items:center;padding-left:19px;font-size:12.5px;border-bottom:1px solid #e6e6e6}
.side-link.last{border-bottom:none;height:70px;align-items:flex-start;padding-top:14px}
.account-row{height:68px;display:flex;align-items:center;justify-content:space-between;padding:0 13px 0 21px;font-size:12.5px}
.label-input{position:absolute;left:7px;top:326px;width:139px;height:32px;border:1px solid #cfcfcf;background:#fff;font-size:10px;padding-left:14px;display:flex;align-items:center;color:#333}
.record-btn{position:absolute;left:7px;top:366px;width:139px;height:28px;background:var(--green);color:#fff;font-size:10px;font-weight:600;display:flex;align-items:center;justify-content:center;letter-spacing:.3px}

.section-title{position:absolute;font-weight:700;font-size:13px;color:#111}
table{border-collapse:collapse;position:absolute;font-size:10.5px;table-layout:fixed}
th{background:var(--head);font-weight:700;height:30px;border:1px solid var(--line);border-top:none}
td{height:32px;border-left:1px solid var(--line);border-right:1px solid var(--line)}
tbody tr:nth-child(even) td{background:var(--row-alt)}
table{border:1px solid var(--line)}
.wallets{left:178px;top:61px;width:760px}
.wallets th:first-child,.wallets td:first-child{text-align:left;padding-left:26px}
.wallets th,.wallets td{text-align:center}
.topup{display:inline-block;background:var(--green);color:#fff;font-weight:600;font-size:10px;padding:3px 8px;letter-spacing:.3px}
.tx{left:181px;top:326px;width:760px;font-size:11.5px}
.tx th{font-size:11px}
.tx td,.tx th{text-align:left;padding-left:18px}
.tx .c{padding-left:28px}

/* footer */
.footer{position:absolute;left:0;top:796px;width:1200px;height:72px;background:var(--white)}
.footer-mark{position:absolute;left:556px;top:759px;width:74px;height:74px;border-radius:50%;background:#fff;box-shadow:0 -1px 3px rgba(0,0,0,.08);display:flex;align-items:center;justify-content:center;font-size:11px;font-weight:600;color:var(--green)}
.copyright{position:absolute;left:0;width:1200px;top:834px;text-align:center;font-size:11.5px;color:#333}
</style>
</head>
<body>
<header class="topbar">
  <div class="brand"><span class="brand-dot"></span><span class="brand-name">Coinvale</span></div>
  <nav class="nav">
    <div class="nav-item active">
      <svg viewBox="0 0 20 20" fill="none" stroke="#fff" stroke-width="1.6"><circle cx="10" cy="10" r="8"/><path d="M10 10l3-4"/><circle cx="10" cy="10" r="1.2" fill="#fff"/></svg>
      DASHBOARD</div>
    <div class="nav-item settings">
      <svg viewBox="0 0 20 20"><path fill="#444" d="M8.6 1h2.8l.4 2.4 1.6.7 2-1.4 2 2-1.4 2 .7 1.6 2.3.4v2.8l-2.3.4-.7 1.6 1.4 2-2 2-2-1.4-1.6.7-.4 2.3H8.6l-.4-2.3-1.6-.7-2 1.4-2-2 1.4-2-.7-1.6L1 11.4V8.6l2.3-.4.7-1.6-1.4-2 2-2 2 1.4 1.6-.7z"/><circle cx="10" cy="10" r="3" fill="#fff"/></svg>
      SETTINGS</div>
    <div class="nav-item notify">
      <svg viewBox="0 0 20 20"><path fill="#444" d="M10 1.5c-3.3 0-5.5 2.5-5.5 5.8v4.2L2.5 15h15l-2-3.5V7.3c0-3.3-2.2-5.8-5.5-5.8z"/><circle cx="10" cy="17" r="2" fill="#444"/></svg>
      NOTIFICATION</div>
    <div class="nav-item signout">
      <svg viewBox="0 0 20 20" fill="none" stroke="#444" stroke-width="1.6"><path d="M8 3h9v14H8"/><path d="M12 10H3M6 7l-3 3 3 3"/></svg>
      SIGN OUT</div>
  </nav>
  <div class="avatar" role="img" aria-label="User profile photo"></div>
  <svg class="chev" width="10" height="7" viewBox="0 0 10 7" fill="none" stroke="#c0262d" stroke-width="1.5"><path d="M1 1l4 4 4-4"/></svg>
</header>

<div class="tabs">
  <div class="tab active">Accounts &amp; Wallet</div>
  <div class="tab">Get Paid</div>
  <div class="tab">Send &amp; Receive</div>
</div>
<div class="tab-rule"></div>

<main class="panel">
  <aside class="sidebar">
    <div class="side-head">GET PAID</div>
    <div class="side-link">Simulate a payment</div>
    <div class="side-link">Generate invoice</div>
    <div class="side-link last">Upload invoice</div>
    <div class="side-head">ACCOUNTS</div>
    <div class="account-row">Richard
      <svg width="12" height="12" viewBox="0 0 12 12" fill="none" stroke="#444" stroke-width="1.1"><path d="M9 7v4H1V3h4"/><path d="M4.5 7.5l.4-1.9L10 .5 11.5 2 6.4 7.1z"/></svg>
    </div>
    <div class="label-input">LABEL</div>
    <div class="record-btn">RECORD NEW ACCOUNT</div>
  </aside>

  <h2 class="section-title" style="left:178px;top:31px">WALLETS</h2>
  <table class="wallets">
    <colgroup><col style="width:195px"><col style="width:211px"><col style="width:173px"><col style="width:181px"></colgroup>
    <thead><tr><th>CURRENCY</th><th>BALANCE</th><th>USD</th><th>MORE...</th></tr></thead>
    <tbody>
      <tr><td>BTC</td><td>0.00000000</td><td>0.15</td><td><span class="topup">TOPUP WALLET</span></td></tr>
      <tr><td>BTC tetnet</td><td>0.00000000</td><td>0.98</td><td><span class="topup">TOPUP WALLET</span></td></tr>
      <tr><td>ETH</td><td>0.00000000</td><td>1.25</td><td><span class="topup">TOPUP WALLET</span></td></tr>
      <tr><td>LTC</td><td>0.00000000</td><td>6.98</td><td><span class="topup">TOPUP WALLET</span></td></tr>
      <tr><td>LTC TESTNET</td><td>0.00000000</td><td>7.58</td><td><span class="topup">TOPUP WALLET</span></td></tr>
    </tbody>
  </table>

  <h2 class="section-title" style="left:179px;top:294px">RECENT TRANSACTIONS</h2>
  <table class="tx">
    <colgroup><col style="width:103px"><col style="width:107px"><col style="width:101px"><col style="width:101px"><col style="width:107px"><col style="width:110px"><col style="width:131px"></colgroup>
    <thead><tr><th class="c">DATE</th><th>CUSTOMER</th><th class="c">INVOICE#</th><th>RECEIVED</th><th class="c">AMOUNT</th><th style="padding-left:12px">EXCHANGE RATE</th><th style="text-align:center;padding:0">INFO</th></tr></thead>
    <tbody>
      <tr><td>31/05/2018</td><td>Richard</td><td class="c">897568</td><td>$58985.00</td><td>$126597.00</td><td class="c">0.015</td><td style="padding-left:12px">lorem ipsum head</td></tr>
      <tr><td>25/05/2018</td><td>Catherine</td><td class="c">568751</td><td>$12548.00</td><td>$58985.00</td><td class="c">0.253</td><td style="padding-left:12px">lorem ipsum head</td></tr>
      <tr><td>15/05/2018</td><td>Mickey</td><td class="c">5478895</td><td>$98789.00</td><td>$12548.00</td><td class="c">1.258</td><td style="padding-left:12px">lorem ipsum</td></tr>
      <tr><td>12/05/2018</td><td>Moore</td><td class="c">897568</td><td>$58985.00</td><td>$98789.00</td><td class="c">0.015</td><td style="padding-left:12px">lorem ipsum head</td></tr>
      <tr><td>11/05/2018</td><td>Ferando</td><td class="c">568751</td><td>$12548.00</td><td>$58985.00</td><td class="c">0.253</td><td style="padding-left:12px">lorem ipsum</td></tr>
    </tbody>
  </table>
</main>

<footer class="footer"></footer>
<div class="footer-mark">Coinvale</div>
<p class="copyright">Copyrights @ 2018 All Rights Reserved</p>
</body>
</html>
```